Criação de Cartao de Visita para Outros
A empresa queria:
" Prestamos serviço para empresas de eletricidades em cabeamento em poste, instalação de fibra na casa do cliente e fusão de fibra. "

```html
<!DOCTYPE html>
<html lang="pt-BR">
<head>
<meta charset="UTF-8">
<title>NEXA Telecom – Cartão de Visita</title>
<link href="https://fonts.googleapis.com/css2?family=Montserrat:wght@400;500;700&display=swap" rel="stylesheet">
<style>
  :root {
    --stage: #8a8d90;
    --navy: #2c3f7a;
    --navy-dark: #243568;
    --navy-light: #34498a;
    --paper: #d9dadc;
    --paper-light: #e6e7e8;
    --paper-shade: #cfd0d2;
    --ink: #4a4d52;
    --white: #ffffff;
  }
  * { margin: 0; padding: 0; box-sizing: border-box; }
  html, body { width: 1200px; height: 1200px; overflow: hidden; }
  body {
    background: var(--stage);
    font-family: "Montserrat", Arial, sans-serif;
    position: relative;
  }
  .card {
    position: absolute;
    left: 180px;
    width: 840px;
    height: 480px;
    overflow: hidden;
    box-shadow: 0 18px 40px rgba(0,0,0,0.25);
  }
  .card-front { top: 100px; background: var(--navy); }
  .card-back  { top: 620px; background: var(--paper); }
  .facets { position: absolute; inset: 0; width: 100%; height: 100%; }

  .brand {
    position: absolute;
    left: 130px;
    top: 190px;
    display: flex;
    align-items: center;
    gap: 26px;
  }
  .brand-square {
    width: 64px; height: 64px;
    background: var(--white);
  }
  .brand-name {
    color: var(--white);
    font-weight: 700;
    font-size: 84px;
    letter-spacing: 4px;
    line-height: 1;
  }
  .brand-tagline {
    position: absolute;
    left: 220px;
    top: 277px;
    color: var(--white);
    font-size: 15px;
    font-weight: 400;
    letter-spacing: 8px;
    text-transform: uppercase;
    opacity: 0.8;
    white-space: nowrap;
  }

  .contact {
    position: absolute;
    left: 70px;
    top: 90px;
    color: var(--ink);
  }
  .contact-name { font-size: 28px; font-weight: 700; }
  .contact-role { font-size: 17px; font-weight: 500; margin-top: 6px; margin-bottom: 44px; }
  .contact-line { font-size: 17px; font-weight: 400; margin-bottom: 14px; }
</style>
</head>
<body>

  <section class="card card-front" aria-label="Frente do cartão">
    <svg class="facets" viewBox="0 0 840 480" aria-hidden="true">
      <polygon points="0,0 320,0 0,300" fill="var(--navy-light)"/>
      <polygon points="520,0 840,0 840,260" fill="var(--navy-dark)"/>
      <polygon points="840,260 840,480 460,480" fill="var(--navy-light)"/>
      <polygon points="0,300 0,480 260,480" fill="var(--navy-dark)"/>
    </svg>
    <div class="brand">
      <span class="brand-square"></span>
      <span class="brand-name">NEXA</span>
    </div>
    <p class="brand-tagline">Telecom Serviços</p>
  </section>

  <section class="card card-back" aria-label="Verso do cartão">
    <svg class="facets" viewBox="0 0 840 480" aria-hidden="true">
      <polygon points="470,0 840,0 840,480 600,480" fill="var(--paper-light)"/>
      <rect x="600" y="140" width="180" height="180" fill="var(--paper-shade)"/>
    </svg>
    <div class="contact">
      <p class="contact-name">Rafael Moura</p>
      <p class="contact-role">Técnico Responsável</p>
      <p class="contact-line">contato@nexatelecom.com</p>
      <p class="contact-line">(11) 3579-2468</p>
      <p class="contact-line">Rua das Acácias, 120</p>
      <p class="contact-line">www.nexatelecom.com</p>
    </div>
  </section>

</body>
</html>
```